依頼詳細
定期的にお客様へ送付させていただく
ハガキのデザインをお願いいたします。

当社はマンション管理を中心に
賃貸仲介、売買不動産仲介を行っています。

今回のハガキの目的はリピート顧客発掘です
・当社にて仲介させていただいたお客様
・管理マンションにご入居いただいたお客様
に定期的におハガキを送付させていただき
・住替え
・買い替え
・知人のご紹介
を促進したいと考えます。
裏面にPRしたいことは当社が
賃貸も売買も管理も全てとりおこなえる事です。

不動産は【固い】イメージですので
アットホームな感じを出したいと思います。
皆様のお力添えよろしくお願いいたします。

デザイン完了後、印刷会社にデザインを届け
ますのでイラレにてデータご提出お願いいたします。

ご参考までに弊社HPもご覧いただき
ご提案いただければ、なお助かります。
http://www.korivale.example/
記載項目
別途添付PDFにて要望記載させていただいております。
希望イメージ
シンプル 複雑
単色 カラフル
暗い 明るい
日常 高級
遊び心 厳粛
未来的 伝統的
女性的 男性的
希望する色
特に決めておりませんが当社ロゴが黄色と黒です。
納品ファイル
• 高解像度JPG (.jpg)
• イラストレーター形式 (.ai)
• フォトショップ形式 (.psd)
• PNG形式 (.png)
■ 選んだ理由

私が、お願いしたイメージ通りに作っていただけたから。
且つ、当社ホームページも見ていただき作りこんで
いただいた感がよりあったため。

■ 提案者全員のお礼・コメント

この度は皆様ご提案ありがとうございました。
今後ともお力添えお願いいたします。

```html
<!DOCTYPE html>
<html lang="ja">
<head>
<meta charset="utf-8">
<title>コリヴェール株式会社 ポストカード</title>
<link rel="stylesheet" href="https://fonts.googleapis.com/css2?family=M+PLUS+Rounded+1c:wght@500;800;900&family=Noto+Sans+JP:wght@500;700;900&display=swap">
<style>
  :root {
    --sky-top: #3f8fd6;
    --sky-mid: #8cc6ee;
    --sky-low: #e3f3fb;
    --ring-red: #e3262f;
    --ring-green: #2fa23a;
    --ring-purple: #8a2c97;
    --ring-orange: #f2891d;
    --ring-blue: #1f6fc2;
    --ring-line: #6fb6e6;
    --ink: #1a1a1a;
    --accent-red: #e5202a;
    --grass: #7cc243;
    --grass-deep: #4f9a2c;
    --panel: #fffdf2;
    --panel-edge: #c9d86a;
    --brand-yellow: #f3c614;
  }
  * { margin: 0; padding: 0; box-sizing: border-box; }
  html, body { width: 810px; height: 1200px; overflow: hidden; background: #fff; }
  .postcard {
    position: relative;
    width: 810px;
    height: 1200px;
    overflow: hidden;
    background: linear-gradient(to bottom, var(--sky-top) 0%, var(--sky-mid) 35%, var(--sky-low) 62%, #f4fae8 100%);
    font-family: "Noto Sans JP", sans-serif;
    color: var(--ink);
  }
  .handshake-photo {
    position: absolute;
    left: 110px; top: 230px;
    width: 640px; height: 430px;
    border-radius: 50%;
    background: radial-gradient(ellipse at 50% 55%, #e8b48f 0%, #d99c78 35%, rgba(217,156,120,0.45) 60%, rgba(217,156,120,0) 75%);
  }
  .meadow-scene {
    position: absolute;
    left: 0; top: 640px;
    width: 810px; height: 560px;
    background:
      radial-gradient(ellipse at 80% 30%, rgba(255,220,160,0.7) 0%, rgba(255,220,160,0) 35%),
      linear-gradient(to bottom, rgba(124,194,67,0) 0%, var(--grass) 30%, var(--grass-deep) 60%, #cfe7a4 100%);
  }
  .service-ring {
    position: absolute;
    left: 0; top: 0;
    width: 810px; height: 900px;
  }
  .ring-label {
    font-family: "M PLUS Rounded 1c", sans-serif;
    font-weight: 900;
    font-size: 60px;
    fill: #fff;
    stroke: rgba(0,0,0,0.35);
    stroke-width: 3px;
    paint-order: stroke;
  }
  .headline-box {
    position: absolute;
    left: 150px; top: 318px;
    width: 540px;
    padding: 14px 0 16px;
    background: rgba(255,255,255,0.88);
    border-radius: 22px;
    text-align: center;
    font-family: "M PLUS Rounded 1c", sans-serif;
    font-weight: 900;
    line-height: 1.22;
  }
  .headline-box .line { display: block; font-size: 46px; color: var(--ink); }
  .headline-box .one-stop { font-size: 70px; color: var(--accent-red); }
  .message-card {
    position: absolute;
    left: 178px; top: 900px;
    width: 380px;
    padding: 14px 18px;
    background: rgba(255,255,255,0.94);
    border: 3px solid var(--panel-edge);
    border-radius: 10px;
    font-size: 22px;
    font-weight: 500;
    line-height: 1.4;
    text-align: center;
  }
  .service-line {
    position: absolute;
    left: 0; top: 1040px;
    width: 810px;
    text-align: center;
    font-size: 30px;
    font-weight: 900;
    letter-spacing: 1px;
  }
  .brand {
    position: absolute;
    left: 0; top: 1092px;
    width: 810px;
    display: flex;
    justify-content: center;
    align-items: center;
    gap: 22px;
  }
  .brand-mark {
    width: 62px; height: 62px;
    background: var(--brand-yellow);
  }
  .brand-name {
    font-family: "Noto Sans JP", sans-serif;
    font-weight: 900;
    font-size: 64px;
    color: var(--ink);
  }
</style>
</head>
<body>
<main class="postcard">
  <div class="handshake-photo" role="img" aria-label="握手する二人の手の写真"></div>
  <div class="meadow-scene" role="img" aria-label="虹と家々、車、草原、家族と高齢夫婦のイラスト"></div>

  <svg class="service-ring" viewBox="0 0 810 900" aria-label="借りたい・貸したい・売りたい・預けたい・買いたい">
    <defs>
      <path id="arc-rent" d="M86.3 241 A368 368 0 0 1 372.9 58.4"/>
      <path id="arc-lease" d="M437.1 58.4 A368 368 0 0 1 723.7 241"/>
      <path id="arc-sell" d="M755 311.3 A368 368 0 0 1 665.2 685.2"/>
      <path id="arc-entrust" d="M86.3 609 A368 368 0 0 0 341.1 787.4"/>
      <path id="arc-buy" d="M59.2 550.9 A368 368 0 0 1 71.5 269.5"/>
    </defs>
    <circle cx="405" cy="425" r="368" fill="none" stroke="var(--ring-line)" stroke-width="12"/>
    <g fill="none" stroke-width="78" stroke-linecap="butt">
      <use href="#arc-rent" stroke="var(--ring-red)"/>
      <use href="#arc-lease" stroke="var(--ring-green)"/>
      <use href="#arc-sell" stroke="var(--ring-purple)"/>
      <use href="#arc-entrust" stroke="var(--ring-orange)"/>
      <use href="#arc-buy" stroke="var(--ring-blue)"/>
    </g>
    <text class="ring-label" dominant-baseline="central" text-anchor="middle"><textPath href="#arc-rent" startOffset="50%">借りたい</textPath></text>
    <text class="ring-label" dominant-baseline="central" text-anchor="middle"><textPath href="#arc-lease" startOffset="50%">貸したい</textPath></text>
    <text class="ring-label" dominant-baseline="central" text-anchor="middle"><textPath href="#arc-sell" startOffset="50%">売りたい</textPath></text>
    <text class="ring-label" dominant-baseline="central" text-anchor="middle"><textPath href="#arc-entrust" startOffset="50%">預けたい</textPath></text>
    <text class="ring-label" dominant-baseline="central" text-anchor="middle"><textPath href="#arc-buy" startOffset="50%">買いたい</textPath></text>
  </svg>

  <h1 class="headline-box">
    <span class="line">お客様のご希望を</span>
    <span class="line"><span class="one-stop">ワンストップ</span>で</span>
    <span class="line">つなぐ会社です!</span>
  </h1>

  <p class="message-card">コリヴェールはオーナー様、<br>ご入居者様とワントゥーワンの<br>お付き合いに注力を注いております。</p>

  <p class="service-line">賃貸・売買不動産仲介マンション・不動産管理</p>

  <div class="brand">
    <span class="brand-mark"></span>
    <span class="brand-name">コリヴェール株式会社</span>
  </div>
</main>
</body>
</html>
```